Brightwell - Self Development Mobile App

Basic Instructions
1. please create an android app screen design for me, in figma, for my new app “Brightwell” based on this pencil drawing (Subjects.jpg)
2. Create the color pallet based on the colors of the logo (#fcd354 and #5dc9b7) and also add shades based on these colors based on material design.
3. the background should be white.
4. Use material design
Get Inspired by wordhopper design and calmnest design
These are the directions i provided for the programmer on how this screen will work:
top bar:
back icon on left (show if you are in a category and press to go back one category)
name of the field in middle in bold
share icon for sharing the current subject on the right before the drop down menu
3 dot icon on the right (drop down menu)
2nd top bar:
fire icon on left for streak (how many days straight did you do a lesson)
star icon a bit after it (how many lessons did you pass)
circles section:
each category will get a section
each category will have a small star with a number that shows how many stars the user has from that category
each category will have an icon before it
under each category there will be circles for all the subjects under that category
scroll horizontally to see more subjects
each subject will have the amount stars gained from it (like the circles of the fields in the fields screen)
scroll down to see more fields with their subjects
note that the order of the subjects and categories should be based on the practial/spiritual score that the user has been assigned based on the initial wizard
More Notes
1. the scribbles in the circles under the following categories (Dreams, Sub-Concious, Feeling)) are just place filers. Please add example content based on the content in the circles that are under “Memory” category
2. There are more sections after Feeling so users should be able to scroll down to see more sections
3. There are more categories to the right so under each section
Final Thoughts
Maybe its better to have rounded cornered squares instead of circles. You choose what you think is best.
After you have created the Subjects screen and I like it, then I'll give you instructions for the other 5 screens.
Target Market(s)
general public, adults 18-80
Font styles to use
Look and feel
Each slider illustrates characteristics of the customer's brand and the style your logo design should communicate.

```html
<!DOCTYPE html>
<html lang="en">
<head>
<meta charset="utf-8">
<title>Brightwell – Mind</title>
<link rel="stylesheet" href="https://fonts.googleapis.com/css2?family=Kumbh+Sans:wght@400;600;700&display=swap">
<style>
  :root {
    --stage: #e9ebe8;
    --white: #ffffff;
    --ink: #2a2a2a;
    --line: #e6e8e6;
    --teal: #4fae94;
    --teal-soft: #d4ece0;
    --teal-mid: #bfe0cd;
    --yellow: #fcd354;
    --mint-top: #eef6f1;
    --cream-bottom: #fbf4d8;
    --ring: #cfe7d9;
  }
  * { box-sizing: border-box; margin: 0; padding: 0; }
  html, body { width: 1200px; height: 675px; overflow: hidden; }
  body {
    background: var(--stage);
    font-family: "Kumbh Sans", sans-serif;
    color: var(--ink);
    position: relative;
  }
  .app-screen {
    position: absolute;
    left: 450px; top: 10px;
    width: 300px; height: 656px;
    border-radius: 34px;
    background: var(--white);
    overflow: hidden;
    box-shadow: 0 6px 24px rgba(0,0,0,.08);
  }
  .top-bar {
    position: absolute; left: 0; top: 0; width: 100%; height: 74px;
    border-bottom: 1px solid var(--line);
  }
  .top-bar .back { position: absolute; left: 14px; top: 34px; }
  .top-bar .menu { position: absolute; right: 14px; top: 28px; }
  .field-title {
    position: absolute; left: 0; right: 0; top: 30px;
    text-align: center; font-size: 20px; font-weight: 600;
  }
  .stats-bar {
    position: absolute; top: 74px; left: 0; width: 100%; height: 51px;
    border-bottom: 1px solid var(--line);
  }
  .stat-pill {
    position: absolute; top: 9px; height: 34px;
    border: 1px solid var(--line); border-radius: 17px;
    display: flex; align-items: center; padding-left: 4px;
    font-size: 13px; font-weight: 600;
  }
  .stat-pill .badge {
    width: 26px; height: 26px; border-radius: 50%;
    display: flex; align-items: center; justify-content: center;
  }
  .stat-pill.streak { left: 61px; width: 75px; }
  .stat-pill.streak .badge { background: var(--yellow); }
  .stat-pill.lessons { left: 146px; width: 83px; }
  .stat-pill.lessons .badge { background: var(--teal); }
  .stat-pill .count { margin-left: 16px; }
  .subjects-area {
    position: absolute; top: 126px; left: 0; width: 100%; bottom: 0;
    background: linear-gradient(180deg, var(--mint-top) 0%, #f3f6ec 55%, var(--cream-bottom) 100%);
    overflow: hidden;
  }
  .arc {
    position: absolute; border-radius: 50%;
  }
  .arc.outer {
    left: 45px; top: 59px; width: 630px; height: 630px;
    background: linear-gradient(180deg, #d6ece0 0%, #e4ecd0 60%, #f2e8b4 100%);
  }
  .arc.inner {
    left: 133px; top: 157px; width: 474px; height: 474px;
    background: linear-gradient(180deg, #bfe0cd 0%, #d6e4c0 55%, #eee4ad 100%);
  }
  .section-title {
    position: absolute; left: 0; right: 0; top: 16px;
    text-align: center; font-size: 19px; font-weight: 600;
  }
  .subject {
    position: absolute; width: 80px; height: 80px; margin: -40px 0 0 -40px;
    border-radius: 50%; background: var(--white);
    border: 1.5px solid var(--ring);
    display: flex; align-items: center; justify-content: center;
  }
  .progress-plant {
    position: absolute; left: 196px; top: 239px; width: 80px; height: 125px;
    border-radius: 14px; background: rgba(79,174,148,.22);
  }
  .progress-value {
    position: absolute; left: 186px; width: 100px; top: 375px;
    text-align: center; font-size: 34px; font-weight: 600; color: var(--teal);
  }
</style>
</head>
<body>
  <main class="app-screen">
    <header class="top-bar">
      <svg class="back" width="16" height="14" viewBox="0 0 16 14" aria-label="Back">
        <path d="M15 7H2M7 1.5 1.5 7 7 12.5" fill="none" stroke="var(--ink)" stroke-width="1.8" stroke-linecap="round" stroke-linejoin="round"/>
      </svg>
      <h1 class="field-title">Mind</h1>
      <svg class="menu" width="6" height="26" viewBox="0 0 6 26" aria-label="More options">
        <circle cx="3" cy="3" r="2.2" fill="var(--ink)"/>
        <circle cx="3" cy="13" r="2.2" fill="var(--ink)"/>
        <circle cx="3" cy="23" r="2.2" fill="var(--ink)"/>
      </svg>
    </header>

    <div class="stats-bar">
      <div class="stat-pill streak">
        <span class="badge">
          <svg width="14" height="16" viewBox="0 0 14 16"><path d="M7 1C8 4 12 6 12 10a5 5 0 0 1-10 0c0-2 1-3.5 2-4.5 0 1.5 1 2.5 2 2.5C5.5 6 6 3.5 7 1Z" fill="none" stroke="#fff" stroke-width="1.5" stroke-linejoin="round"/></svg>
        </span>
        <span class="count">2</span>
      </div>
      <div class="stat-pill lessons">
        <span class="badge">
          <svg width="14" height="14" viewBox="0 0 24 24"><path d="M12 2l2.9 6.6 7.1.6-5.4 4.7 1.6 7L12 17.3 5.8 20.9l1.6-7L2 9.2l7.1-.6Z" fill="#fff"/></svg>
        </span>
        <span class="count">34</span>
      </div>
    </div>

    <section class="subjects-area">
      <div class="arc outer"></div>
      <div class="arc inner"></div>
      <h2 class="section-title">Foundation</h2>

      <div class="subject" style="left:141px;top:96px">
        <svg width="30" height="30" viewBox="0 0 30 30" aria-label="Entry">
          <path d="M5 27V4l13-2v25Z" fill="var(--teal)"/>
          <path d="M18 4h5v22h3" fill="none" stroke="var(--teal)" stroke-width="2.4"/>
          <rect x="2" y="25.5" width="17" height="2.5" fill="var(--teal)"/>
          <rect x="12" y="13" width="2.5" height="4" fill="#fff"/>
        </svg>
      </div>
      <div class="subject" style="left:89px;top:179px">
        <svg width="34" height="30" viewBox="0 0 34 30" aria-label="Reading">
          <path d="M2 7h13v20H2Z" fill="var(--yellow)"/>
          <path d="M17 27V7l12-5v21Z" fill="var(--yellow)"/>
          <path d="M31 7v20H17" fill="none" stroke="var(--yellow)" stroke-width="2"/>
          <path d="M23 7v14" stroke="#fff" stroke-width="2"/>
        </svg>
      </div>
      <div class="subject" style="left:61px;top:272px">
        <svg width="28" height="34" viewBox="0 0 28 34" aria-label="Stop">
          <path d="M5 8a2 2 0 0 1 4 0v8V4a2 2 0 0 1 4 0v12V3a2 2 0 0 1 4 0v13V6a2 2 0 0 1 4 0v14l2-4a2 2 0 0 1 3.5 2l-4 9a8 8 0 0 1-7.5 5h-2A8 8 0 0 1 5 25Z" fill="var(--teal)"/>
          <path d="M9 10v8M13 8v9M17 8v9" stroke="#fff" stroke-width="1.2"/>
        </svg>
      </div>
      <div class="subject" style="left:59px;top:379px">
        <svg width="38" height="30" viewBox="0 0 38 30" aria-label="Lesson">
          <path d="M2 4c5-2 10-2 16 1v23c-6-3-11-3-16-1Z" fill="var(--yellow)"/>
          <path d="M20 5c6-3 11-3 16-1v23c-5-2-10-2-16 1Z" fill="none" stroke="var(--yellow)" stroke-width="2.2"/>
          <path d="M24 10h8M24 14h8M24 18h8M24 22h8" stroke="var(--yellow)" stroke-width="1.6"/>
        </svg>
      </div>
      <div class="subject" style="left:89px;top:474px">
        <svg width="32" height="32" viewBox="0 0 24 24" aria-label="Review">
          <path d="M12 2l2.9 6.6 7.1.6-5.4 4.7 1.6 7L12 17.3 5.8 20.9l1.6-7L2 9.2l7.1-.6Z" fill="var(--teal)"/>
        </svg>
      </div>
      <div class="subject" style="left:146px;top:548px"></div>

      <div class="progress-plant" role="img" aria-label="Line drawing of a sprouting plant in a pot showing section growth"></div>
      <p class="progress-value">70%</p>
    </section>
  </main>
</body>
</html>
```